Educational Management System User Interface (Veltrix Design Concepts)

Hi,I require a 1-page design for an educational management system. The image attached shows all required elements and also their locations. I require the design to be based on veltrix-styled interfaces using elements from: http://pramel.examplehost.io/pramel-framekit/ & http://kitnulloa.com/kitnulloa-layout/admin . Side menu's should not be too large that they hide the main content of the page.
Sorry very slight addition to the design as per new uploaded file.
I like how the elements of the veltrix orbit page are seperated with the background colour and white boxes. This could maybe work in the design as per the uploaded image?
Thanks,
Tobias
Reason: Some designers have some submissions.

```html
<!DOCTYPE html>
<html lang="en">
<head>
<meta charset="utf-8">
<title>Coursely – Teacher Dashboard</title>
<link rel="stylesheet" href="https://fonts.googleapis.com/css2?family=Open+Sans:wght@300;400;600;700&display=swap">
<style>
:root{
  --bg:#ebeef3;
  --panel:#ffffff;
  --line:#e6e9ee;
  --text:#4a4a4a;
  --muted:#9aa3ad;
  --heading:#8f9aa6;
  --brand:#4a86cc;
  --green:#86c34b;
  --alert:#f0613f;
  --icon:#5f6266;
  --link:#3a9ad9;
  --rail:#c8d0da;
  --shadow:0 1px 2px rgba(0,0,0,.08);
}
*{box-sizing:border-box;margin:0;padding:0}
html,body{width:1024px;height:1200px;overflow:hidden}
body{background:var(--bg);font-family:"Open Sans",Arial,sans-serif;color:var(--text);position:relative}
.abs{position:absolute}
.topbar{left:0;top:0;width:1024px;height:59px;background:var(--panel);border-bottom:1px solid #dde2e8}
.brand{left:24px;top:14px;font-size:24px;font-weight:700;color:var(--brand);letter-spacing:.5px}
.nav-icon{top:18px}
.badge{width:12px;height:12px;border-radius:50%;background:var(--alert);color:#fff;font-size:8px;line-height:12px;text-align:center}
.user-name{left:922px;top:21px;font-size:12px;color:#666}
.avatar-photo{background:linear-gradient(160deg,#e7c28f 0%,#d59a67 45%,#f2d3b1 100%)}
.avatar-self{background:linear-gradient(160deg,#6d5a43 0%,#b08e6b 50%,#3f3a36 100%)}
.avatar-user{background:linear-gradient(160deg,#e2e2e2,#8c8c8c)}

.sidebar{left:0;top:77px;width:179px;height:473px;background:var(--panel);box-shadow:var(--shadow)}
.sidebar-title{position:absolute;left:18px;top:16px;font-size:24px;font-weight:300;color:var(--heading)}
.section-head{position:absolute;left:20px;display:flex;align-items:center;gap:8px;font-size:13px;color:var(--heading)}
.menu-row{position:absolute;left:0;width:179px;height:33px;border-top:1px solid var(--line);font-size:11.5px;line-height:32px;padding-left:22px;color:#444}
.btn-green{position:absolute;left:19px;width:112px;height:26px;background:var(--green);color:#fff;font-size:9.5px;line-height:26px;text-align:center;border-radius:1px}

.refine{left:602px;top:78px;width:160px;height:28px;background:var(--panel);border:1px solid #e2e6eb;font-size:11.5px;line-height:26px;padding-left:10px;color:#444}
.refine svg{position:absolute;right:10px;top:11px}

.composer{left:204px;top:114px;width:560px;height:128px;background:var(--panel);box-shadow:var(--shadow)}
.composer-input{position:absolute;left:80px;top:32px;width:456px;height:27px;border:1px solid #e1e5ea;font-size:11px;line-height:25px;padding-left:12px;color:#999}
.btn-post{position:absolute;left:424px;top:71px;width:112px;height:27px;background:var(--green);color:#fff;font-size:11.5px;line-height:27px;text-align:center}
.tool{position:absolute;top:79px}

.timeline{left:239px;top:282px;width:2px;height:918px;background:var(--rail)}

.post{position:absolute;background:var(--panel);box-shadow:var(--shadow);height:130px}
.post::before{content:"";position:absolute;left:-8px;top:42px;border-style:solid;border-width:8px 8px 8px 0;border-color:transparent var(--panel) transparent transparent}
.post .author{position:absolute;top:21px;font-size:11.5px;color:#444}
.post .date{position:absolute;right:20px;top:22px;font-size:11px;color:var(--muted)}
.post .body{position:absolute;top:45px;right:20px;font-size:11.3px;line-height:16px;color:#555}
.post .reply{position:absolute;right:16px;bottom:13px}
.post.nested .author{top:28px}
.post.nested .date{top:29px}
.post.nested .body{top:52px}
.post.file .author,.post.file .date{top:21px}
.file-icon{position:absolute;left:20px;top:23px;text-align:center}
.file-icon span{display:block;font-size:9px;font-weight:600;color:var(--link);margin-top:2px}

.events{left:792px;top:78px;width:188px;height:472px;background:var(--panel);box-shadow:var(--shadow)}
.events-title{position:absolute;left:0;width:188px;text-align:center;font-size:13px;font-weight:300;color:var(--heading)}
.event{position:absolute;left:0;width:188px;height:33px;font-size:11.3px;line-height:33px;padding-left:14px;color:#444;white-space:nowrap}
.event.sep{border-bottom:1px solid var(--line)}
.event .bar{color:#999;margin:0 6px}
.event svg{vertical-align:-1px;margin-left:2px}
</style>
</head>
<body>

<header class="abs topbar">
  <div class="abs brand">Coursely</div>
  <svg class="abs nav-icon" style="left:204px" width="26" height="24" viewBox="0 0 26 24"><path d="M13 2 1 13h4v10h6v-7h4v7h6V13h4z" fill="var(--icon)"/></svg>
  <svg class="abs nav-icon" style="left:244px;top:19px" width="24" height="24" viewBox="0 0 24 24"><rect x="1" y="3" width="22" height="20" fill="none" stroke="var(--icon)" stroke-width="2"/><rect x="1" y="3" width="22" height="5" fill="var(--icon)"/><g fill="var(--icon)"><rect x="4" y="11" width="3" height="3"/><rect x="9" y="11" width="3" height="3"/><rect x="14" y="11" width="3" height="3"/><rect x="19" y="11" width="2" height="3"/><rect x="4" y="16" width="3" height="3"/><rect x="9" y="16" width="3" height="3"/><rect x="14" y="16" width="3" height="3"/></g></svg>
  <svg class="abs nav-icon" style="left:281px" width="28" height="22" viewBox="0 0 28 22"><path d="M2 11l5-5 6 6L23 2l4 4-14 14z" fill="var(--icon)"/></svg>
  <svg class="abs nav-icon" style="left:322px;top:20px" width="30" height="22" viewBox="0 0 30 22"><path d="M1 2h9l3 3h12v4H7L1 20z" fill="var(--icon)"/><path d="M7 10h22l-6 11H1z" fill="var(--icon)"/></svg>

  <svg class="abs" style="left:810px;top:22px" width="18" height="16" viewBox="0 0 18 16"><path d="M9 1 17 15H1z" fill="var(--icon)"/><rect x="8" y="6" width="2" height="5" fill="#fff"/><rect x="8" y="12" width="2" height="2" fill="#fff"/></svg>
  <div class="abs badge" style="left:807px;top:21px">6</div>
  <svg class="abs" style="left:850px;top:25px" width="16" height="12" viewBox="0 0 16 12"><rect width="16" height="12" fill="var(--icon)"/><path d="M0 0l8 7 8-7" fill="none" stroke="#fff" stroke-width="1.5"/></svg>
  <div class="abs badge" style="left:848px;top:21px">5</div>
  <div class="abs avatar-user" style="left:890px;top:18px;width:22px;height:22px" role="img" aria-label="Profile photo of John Doe"></div>
  <div class="abs user-name">John Doe <svg width="8" height="6" viewBox="0 0 8 6"><path d="M1 1l3 3 3-3" fill="none" stroke="#777" stroke-width="1.3"/></svg></div>
</header>

<aside class="abs sidebar">
  <div class="sidebar-title">Teacher</div>
  <div class="section-head" style="top:64px"><svg width="24" height="16" viewBox="0 0 24 16"><circle cx="8" cy="4" r="4" fill="var(--heading)"/><path d="M0 16c0-5 3-7 8-7s8 2 8 7z" fill="var(--heading)"/><circle cx="16" cy="4" r="3.5" fill="var(--heading)"/><path d="M17 9c4 0 7 2 7 7h-6c0-3-1-5-3-6z" fill="var(--heading)"/></svg>My Groups</div>
  <div class="menu-row" style="top:97px">Group Name</div>
  <div class="menu-row" style="top:129px">Group Name</div>
  <div class="menu-row" style="top:162px">Group Name</div>
  <div class="menu-row" style="top:195px">Group Name</div>
  <div class="menu-row" style="top:228px;height:1px"></div>
  <div class="btn-green" style="top:243px">Create New Group</div>
  <div class="btn-green" style="top:275px">Join More Group</div>
  <div class="section-head" style="top:331px"><svg width="26" height="16" viewBox="0 0 26 16"><circle cx="13" cy="4" r="4" fill="var(--heading)"/><path d="M5 16c0-5 3-7 8-7s8 2 8 7z" fill="var(--heading)"/><circle cx="5" cy="5" r="3" fill="var(--heading)"/><circle cx="21" cy="5" r="3" fill="var(--heading)"/><path d="M0 15c0-4 2-6 5-6l2 1c-2 1-3 3-3 5z M26 15c0-4-2-6-5-6l-2 1c2 1 3 3 3 5z" fill="var(--heading)"/></svg>Community</div>
  <div class="menu-row" style="top:363px">Study Owl</div>
  <div class="menu-row" style="top:396px;height:1px"></div>
</aside>

<div class="abs refine">Refine by Group<svg width="6" height="4" viewBox="0 0 6 4"><path d="M0 0h6L3 4z" fill="#333"/></svg></div>

<section class="abs composer">
  <div class="abs avatar-self" style="left:23px;top:31px;width:51px;height:51px" role="img" aria-label="Profile photo of the teacher"></div>
  <div class="composer-input">Post New Update...</div>
  <svg class="tool" style="left:337px" width="12" height="12" viewBox="0 0 12 12"><circle cx="4" cy="4" r="2.6" fill="none" stroke="var(--icon)" stroke-width="1.4"/><circle cx="8" cy="8" r="2.6" fill="none" stroke="var(--icon)" stroke-width="1.4"/></svg>
  <svg class="tool" style="left:366px" width="10" height="12" viewBox="0 0 10 12"><path d="M1 1h5l3 3v7H1z" fill="none" stroke="var(--icon)" stroke-width="1.3"/></svg>
  <svg class="tool" style="left:392px" width="14" height="12" viewBox="0 0 14 12"><path d="M1 3h3l1-2h4l1 2h3v8H1z" fill="var(--icon)"/><circle cx="7" cy="7" r="2.3" fill="#fff"/></svg>
  <div class="btn-post">Post</div>
</section>

<div class="abs timeline"></div>
<svg class="abs" style="left:231px;top:264px" width="18" height="17" viewBox="0 0 18 17"><path d="M15 6A6.5 6.5 0 0 0 3 5" fill="none" stroke="var(--link)" stroke-width="2.4"/><path d="M3 11a6.5 6.5 0 0 0 12 1" fill="none" stroke="var(--link)" stroke-width="2.4"/><path d="M17 1v6h-6z M1 16v-6h6z" fill="var(--link)"/></svg>

<!-- feed -->
<div class="abs avatar-photo" style="left:214px;top:311px;width:52px;height:51px" role="img" aria-label="Profile photo of Anna Molly"></div>
<article class="post" style="left:284px;top:281px;width:480px">
  <div class="author" style="left:17px">Anna Molly</div><div class="date">12 Dec, 2014 at 12:10</div>
  <p class="body" style="left:17px">Cras sit amet nibh libero, in gravida nulla. Nulla vel metus scelerisque ante sollicitudin commodo. Cras purus odio, vestibulum in vulputate at, tempus viverra turpis.</p>
  <svg class="reply" width="12" height="10" viewBox="0 0 12 10"><path d="M5 0 0 4l5 4V5c3 0 5 1 7 5 0-5-3-7-7-7z" fill="var(--link)"/></svg>
</article>

<div class="abs avatar-photo" style="left:288px;top:457px;width:51px;height:51px" role="img" aria-label="Profile photo of Anna Molly"></div>
<article class="post nested" style="left:356px;top:420px;width:408px">
  <div class="author" style="left:18px">Anna Molly</div><div class="date">12 Dec, 2014 at 12:10</div>
  <p class="body" style="left:18px">Cras sit amet nibh libero, in gravida nulla. Nulla vel metus scelerisque ante sollicitudin commodo. Cras purus odio, vestibulum in vulputate at, tempus viverra turpis.</p>
  <svg class="reply" width="12" height="10" viewBox="0 0 12 10"><path d="M5 0 0 4l5 4V5c3 0 5 1 7 5 0-5-3-7-7-7z" fill="var(--link)"/></svg>
</article>

<div class="abs avatar-photo" style="left:214px;top:614px;width:52px;height:51px" role="img" aria-label="Profile photo of Anna Molly"></div>
<article class="post file" style="left:284px;top:584px;width:480px">
  <div class="file-icon"><svg width="44" height="52" viewBox="0 0 44 52"><path d="M2 2h28l12 12v36H2z" fill="none" stroke="#4d5660" stroke-width="2.4"/><path d="M30 2v12h12" fill="none" stroke="#4d5660" stroke-width="2"/><circle cx="20" cy="32" r="9" fill="none" stroke="#4d5660" stroke-width="2.4"/><path d="M20 32V23 M20 32h9" stroke="#4d5660" stroke-width="2.4"/><path d="M25 21l8 -4v8z" fill="none" stroke="#4d5660" stroke-width="2"/></svg><span>results.pdf</span></div>
  <div class="author" style="left:89px">Anna Molly</div><div class="date">12 Dec, 2014 at 12:10</div>
  <p class="body" style="left:89px">Cras sit amet nibh libero, in gravida nulla. Nulla vel metus scelerisque ante sollicitudin commodo. Cras purus odio, vestibulum in vulputate at, tempus viverra turpis.</p>
  <svg class="reply" width="12" height="10" viewBox="0 0 12 10"><path d="M5 0 0 4l5 4V5c3 0 5 1 7 5 0-5-3-7-7-7z" fill="var(--link)"/></svg>
</article>

<div class="abs avatar-photo" style="left:214px;top:790px;width:52px;height:51px" role="img" aria-label="Profile photo of Anna Molly"></div>
<article class="post" style="left:284px;top:760px;width:480px">
  <div class="author" style="left:17px">Anna Molly</div><div class="date">12 Dec, 2014 at 12:10</div>
  <p class="body" style="left:17px">Cras sit amet nibh libero, in gravida nulla. Nulla vel metus scelerisque ante sollicitudin commodo. Cras purus odio, vestibulum in vulputate at, tempus viverra turpis.</p>
  <svg class="reply" width="12" height="10" viewBox="0 0 12 10"><path d="M5 0 0 4l5 4V5c3 0 5 1 7 5 0-5-3-7-7-7z" fill="var(--link)"/></svg>
</article>

<div class="abs avatar-photo" style="left:214px;top:957px;width:52px;height:51px" role="img" aria-label="Profile photo of Anna Molly"></div>
<article class="post" style="left:284px;top:926px;width:480px">
  <div class="author" style="left:17px">Anna Molly</div><div class="date">12 Dec, 2014 at 12:10</div>
  <p class="body" style="left:17px">Cras sit amet nibh libero, in gravida nulla. Nulla vel metus scelerisque ante sollicitudin commodo. Cras purus odio, vestibulum in vulputate at, tempus viverra turpis.</p>
  <svg class="reply" width="12" height="10" viewBox="0 0 12 10"><path d="M5 0 0 4l5 4V5c3 0 5 1 7 5 0-5-3-7-7-7z" fill="var(--link)"/></svg>
</article>

<div class="abs avatar-photo" style="left:288px;top:1102px;width:51px;height:51px" role="img" aria-label="Profile photo of Anna Molly"></div>
<article class="post nested" style="left:356px;top:1066px;width:408px">
  <div class="author" style="left:18px">Anna Molly</div><div class="date">12 Dec, 2014 at 12:10</div>
  <p class="body" style="left:18px">Cras sit amet nibh libero, in gravida nulla. Nulla vel metus scelerisque ante sollicitudin commodo. Cras purus odio, vestibulum in vulputate at, tempus viverra turpis.</p>
  <svg class="reply" width="12" height="10" viewBox="0 0 12 10"><path d="M5 0 0 4l5 4V5c3 0 5 1 7 5 0-5-3-7-7-7z" fill="var(--link)"/></svg>
</article>

<aside class="abs events">
  <div class="events-title" style="top:27px">Today's Events</div>
  <div class="event sep" style="top:62px">12:15<span class="bar">|</span>Meeting in Canteen <svg width="9" height="9" viewBox="0 0 9 9"><circle cx="4.5" cy="4.5" r="4.5" fill="var(--alert)"/><rect x="4" y="4" width="1.2" height="3" fill="#fff"/><rect x="4" y="2" width="1.2" height="1.2" fill="#fff"/></svg></div>
  <div class="event sep" style="top:94px">12:15<span class="bar">|</span>Meeting in Canteen <svg width="9" height="9" viewBox="0 0 9 9"><circle cx="4.5" cy="4.5" r="4.5" fill="var(--alert)"/><rect x="4" y="4" width="1.2" height="3" fill="#fff"/><rect x="4" y="2" width="1.2" height="1.2" fill="#fff"/></svg></div>
  <div class="event sep" style="top:127px">12:15<span class="bar">|</span>Meeting in Canteen <svg width="9" height="9" viewBox="0 0 9 9"><circle cx="4.5" cy="4.5" r="4.5" fill="var(--alert)"/><rect x="4" y="4" width="1.2" height="3" fill="#fff"/><rect x="4" y="2" width="1.2" height="1.2" fill="#fff"/></svg></div>
  <div class="event sep" style="top:159px">12:15<span class="bar">|</span>Meeting in Canteen <svg width="9" height="9" viewBox="0 0 9 9"><circle cx="4.5" cy="4.5" r="4.5" fill="var(--alert)"/><rect x="4" y="4" width="1.2" height="3" fill="#fff"/><rect x="4" y="2" width="1.2" height="1.2" fill="#fff"/></svg></div>
  <div class="event sep" style="top:192px">12:15<span class="bar">|</span>Meeting in Canteen <svg width="9" height="9" viewBox="0 0 9 9"><circle cx="4.5" cy="4.5" r="4.5" fill="var(--alert)"/><rect x="4" y="4" width="1.2" height="3" fill="#fff"/><rect x="4" y="2" width="1.2" height="1.2" fill="#fff"/></svg></div>

  <div class="events-title" style="top:265px">Upcoming Events</div>
  <div class="event sep" style="top:301px">12:15<span class="bar">|</span>Meeting in Canteen <svg width="9" height="9" viewBox="0 0 9 9"><circle cx="4.5" cy="4.5" r="4.5" fill="var(--alert)"/><rect x="4" y="4" width="1.2" height="3" fill="#fff"/><rect x="4" y="2" width="1.2" height="1.2" fill="#fff"/></svg></div>
  <div class="event sep" style="top:333px">12:15<span class="bar">|</span>Meeting in Canteen <svg width="9" height="9" viewBox="0 0 9 9"><circle cx="4.5" cy="4.5" r="4.5" fill="var(--alert)"/><rect x="4" y="4" width="1.2" height="3" fill="#fff"/><rect x="4" y="2" width="1.2" height="1.2" fill="#fff"/></svg></div>
  <div class="event sep" style="top:366px">12:15<span class="bar">|</span>Meeting in Canteen <svg width="9" height="9" viewBox="0 0 9 9"><circle cx="4.5" cy="4.5" r="4.5" fill="var(--alert)"/><rect x="4" y="4" width="1.2" height="3" fill="#fff"/><rect x="4" y="2" width="1.2" height="1.2" fill="#fff"/></svg></div>
  <div class="event sep" style="top:398px">12:15<span class="bar">|</span>Meeting in Canteen <svg width="9" height="9" viewBox="0 0 9 9"><circle cx="4.5" cy="4.5" r="4.5" fill="var(--alert)"/><rect x="4" y="4" width="1.2" height="3" fill="#fff"/><rect x="4" y="2" width="1.2" height="1.2" fill="#fff"/></svg></div>
  <div class="event" style="top:431px">12:15<span class="bar">|</span>Meeting in Canteen <svg width="9" height="9" viewBox="0 0 9 9"><circle cx="4.5" cy="4.5" r="4.5" fill="var(--alert)"/><rect x="4" y="4" width="1.2" height="3" fill="#fff"/><rect x="4" y="2" width="1.2" height="1.2" fill="#fff"/></svg></div>
</aside>

</body>
</html>
```